Carpet Cleaning & Car Detailing. I don't have a logo design yet. I like electric blue black and white as the colours.

We clean:

- Carpets
- rugs

We have added the car detailing to the bussiness

- car detailing
- seat cleaning
- carpet cleaning

Industry/Entity Type

Carpet

Contact Information for Business Card

morvancarpetcleaning@quillbox.net
0491 628 307

```html
<!DOCTYPE html>
<html lang="en">
<head>
<meta charset="utf-8">
<title>Morvan Carpet Cleaning &amp; Car Detailing – Business Card</title>
<link rel="stylesheet" href="https://fonts.googleapis.com/css2?family=Questrial&family=Ropa+Sans&family=Tinos:wght@400;700&display=swap">
<style>
  :root {
    --page: #ffffff;
    --card: #ffffff;
    --card-edge: #8a8a8a;
    --ink: #111111;
    --brand-blue: #0a72bb;
    --on-blue: #ffffff;
  }
  * { margin: 0; padding: 0; box-sizing: border-box; }
  html, body {
    width: 1200px;
    height: 1000px;
    overflow: hidden;
    background: var(--page);
  }
  .canvas {
    position: relative;
    width: 1200px;
    height: 1000px;
  }
  .business-card {
    position: absolute;
    left: 201px;
    top: 238px;
    width: 809px;
    height: 431px;
    background: var(--card);
    border: 1px solid var(--card-edge);
  }
  .brand {
    position: absolute;
    left: 60px;
    top: 120px;
    font-family: "Questrial", sans-serif;
    color: var(--ink);
  }
  .brand-dot {
    position: absolute;
    left: 0;
    top: 22px;
    width: 36px;
    height: 36px;
    border-radius: 50%;
    background: var(--brand-blue);
  }
  .brand-name {
    position: absolute;
    left: 56px;
    top: 0;
    font-size: 62px;
    line-height: 70px;
    white-space: nowrap;
  }
  .brand-tagline {
    position: absolute;
    left: 40px;
    top: 72px;
    font-size: 33px;
    line-height: 34px;
    white-space: nowrap;
  }
  .brand-tagline .second { padding-left: 62px; display: block; }
  .divider {
    position: absolute;
    left: 445px;
    top: 23px;
    width: 3px;
    height: 300px;
    background: var(--ink);
  }
  .services {
    position: absolute;
    left: 491px;
    top: 24px;
    color: var(--ink);
  }
  .services-title {
    font-family: "Tinos", serif;
    font-weight: 700;
    font-size: 37px;
    line-height: 46px;
    padding-left: 10px;
    letter-spacing: 0.5px;
  }
  .services-list {
    list-style: none;
    margin-top: 18px;
    font-family: "Ropa Sans", sans-serif;
    font-size: 37px;
    line-height: 47px;
  }
  .contact-band {
    position: absolute;
    left: 0;
    top: 364px;
    width: 807px;
    height: 51px;
    background: var(--brand-blue);
    color: var(--on-blue);
    font-family: "Tinos", serif;
    display: flex;
    align-items: center;
    padding-left: 12px;
    white-space: nowrap;
  }
  .contact-email { font-size: 25px; }
  .contact-star { margin: 0 12px 0 14px; display: block; }
  .contact-phone { font-size: 29px; letter-spacing: 0.5px; }
</style>
</head>
<body>
<div class="canvas">
  <section class="business-card">
    <div class="brand">
      <span class="brand-dot"></span>
      <div class="brand-name">Morvan</div>
      <div class="brand-tagline">Carpet Cleaning &amp;<span class="second">Car Detailing</span></div>
    </div>

    <div class="divider"></div>

    <div class="services">
      <h2 class="services-title">Our Services</h2>
      <ul class="services-list">
        <li>* Carpet Cleaning</li>
        <li>* Rug Cleaning</li>
        <li>* Car Detailing</li>
        <li>* Seat Cleaning</li>
        <li>And Much More...</li>
      </ul>
    </div>

    <div class="contact-band">
      <span class="contact-email">morvancarpetcleaning@quillbox.net</span>
      <svg class="contact-star" width="24" height="24" viewBox="0 0 24 24" aria-hidden="true">
        <polygon fill="var(--on-blue)" points="12,1 15,9 23,9 16.5,14 19,22 12,17 5,22 7.5,14 1,9 9,9"/>
      </svg>
      <span class="contact-phone">Phone: 0491 628 307</span>
    </div>
  </section>
</div>
</body>
</html>
```